Pathwell | An Alcolohism Recovery Blogging Site

Pathwell.com.au is a blog based on alcoholism. Primarily, alcholics who are in sobreity, or recovery. The blog posts are centred around this and are written by other alcholics who share their thoughts, strenght, experience, thoeries on how to get sober, and stay sober, but primarily, live a better life in active sobriety. The site provides information related to CR and other services/groups that assist in alcolohism. We write E-Books and sell these also. Pathwell strives to be a blog that alcoholics want to read, and get strength and hope from reading it, and the posts from other users. We want to be easy to use, simple to navigate and sharply designed. We want the site to be cutting edge and appealing. We want to engage the audience from the first moment they hit the page, no matter where they land. I like this website as a model for a wordpress site making good use of simplicity = thriftlane.com.au

Target Market(s)

People who might think they have a problem with Alcohol, people who are alcholics looking at entering rehab or recovery, people that are alcoholics in recovery already

Requirements
Must have
• simplicity, large fonts for headings, space for advertising through ad words and other forms, nice large navigation across the top, a sharp, html 5 feel, i want to be using great fonts and nice/sheek.
Nice to have
• logo will be used in print as well as online. It would be VERY GOOD to have someone design a ecover for my ebook i will be selling on this website. the book is titled "THE CLEAR MORNING PROMISE - The Gentle Path to finding calm and keeping it for good!"
Should not have
• do not include illustrations of alcohol.

```html
<!DOCTYPE html>
<html lang="en">
<head>
<meta charset="utf-8">
<title>Pathwell – Getting back on track</title>
<link rel="stylesheet" href="https://fonts.googleapis.com/css2?family=Noto+Sans:wght@400;700&family=Comfortaa:wght@400&display=swap">
<style>
:root{
  --page-cream:#efe9c4;
  --stone-dark:#3c3c3e;
  --stone-mid:#5a5a5c;
  --bar-top:#5c5c6e;
  --bar-bottom:#3e3e4e;
  --panel-grey:#a8a9ab;
  --gold:#f2c055;
  --gold-link:#c99a1e;
  --title-blue:#3d4a70;
  --ink:#2a2a2a;
  --card-top:#ffffff;
  --card-bottom:#dedede;
  --social-orange:#e8821e;
  --social-blue:#3b5ea8;
  --social-sky:#3d8fd1;
}
*{box-sizing:border-box;margin:0;padding:0}
html,body{width:1095px;height:1200px;overflow:hidden}
body{
  position:relative;
  background:var(--page-cream);
  font-family:"Noto Sans",Verdana,sans-serif;
  color:var(--ink);
}
.header-band{
  position:absolute;left:0;top:22px;width:1095px;height:212px;
  background:radial-gradient(ellipse at 30% 40%,#5e5e60 0%,var(--stone-dark) 70%);
}
.top-strip{position:absolute;left:0;top:0;width:1095px;height:22px;background:#fff}
.footer-band{
  position:absolute;left:0;top:1107px;width:1095px;height:93px;
  background:radial-gradient(ellipse at 50% 50%,#626264 0%,var(--stone-dark) 80%);
}
.brand{
  position:absolute;left:40px;top:70px;
  display:flex;align-items:center;gap:16px;
}
.brand-mark{width:34px;height:34px;border-radius:50%;background:var(--gold)}
.brand-name{font-size:62px;font-weight:400;color:var(--gold);letter-spacing:1px}
.tagline{
  position:absolute;left:358px;top:158px;
  font-family:"Comfortaa",sans-serif;font-size:36px;color:#e2e2e2;letter-spacing:1px;
}
.site-frame{
  position:absolute;left:89px;top:209px;width:911px;height:858px;
  background:var(--panel-grey);border-radius:12px;
  box-shadow:0 3px 8px rgba(0,0,0,.35);
}
.main-nav{
  height:48px;border-radius:12px 12px 0 0;
  background:linear-gradient(var(--bar-top),var(--bar-bottom));
  display:flex;align-items:center;padding-left:25px;
}
.main-nav a{font-size:27px;color:#fff;text-decoration:none;margin-right:55px}
.main-nav a.current{color:var(--gold)}
.search{
  margin-left:auto;margin-right:26px;display:flex;
  width:171px;height:24px;border-radius:4px;overflow:hidden;background:#fff;
}
.search span{flex:1;font-size:13px;color:#888;padding:3px 13px}
.search i{width:30px;background:#9a9a9a;display:flex;align-items:center;justify-content:center}
.column{position:absolute;top:82px;display:flex;flex-direction:column}
.col-left{left:15px;width:205px}
.col-center{left:231px;width:456px}
.col-right{left:699px;width:204px}
.card{
  border-radius:9px;overflow:hidden;
  background:linear-gradient(var(--card-top) 55%,var(--card-bottom));
  box-shadow:0 2px 4px rgba(0,0,0,.35);
  border:1px solid #8c8c8c;
}
.card-head{
  height:43px;padding:0 11px;
  background:linear-gradient(var(--bar-top),var(--bar-bottom));
  font-size:31px;color:var(--gold);line-height:43px;
}
.card-body{padding:12px 12px 10px;font-size:13.3px;line-height:22px}
.ebook-body{height:179px;position:relative}
.ebook-cover{
  display:block;margin:8px auto 0;width:98px;height:95px;border-radius:3px;
  background:linear-gradient(135deg,#e6e6e6,#bdbdbd);
}
.btn{
  display:inline-block;border-radius:9px;
  background:linear-gradient(#5c5c6c,#35353f);color:var(--gold);
  text-align:center;text-decoration:none;
}
.btn-download{position:absolute;left:4px;right:4px;bottom:6px;height:35px;line-height:35px;font-size:19px}
.link-list{padding:14px 16px 8px}
.link-list h4{font-size:15px;font-weight:400;text-decoration:underline;color:#111;margin-bottom:2px}
.link-list a{display:block;font-size:11px;line-height:22px;color:var(--gold-link);padding-left:8px}
.ads-body{height:163px}
.links-body{height:163px}
.gap{height:16px}
.welcome-body{height:168px;padding:25px 17px;font-size:13px;line-height:22px}
.blog-body{height:476px;padding:14px 20px 0;position:relative}
.post-title{font-size:33px;font-weight:400;color:var(--title-blue);line-height:42px}
.post-meta{font-size:11.5px;margin:4px 0 12px}
.post-meta a{color:var(--gold-link);text-decoration:none}
.post-row{display:flex;gap:15px}
.post-photo{width:122px;height:124px;flex:none;border:1px solid #777;background:linear-gradient(#dfe6ec,#b9c6d2)}
.post-text{font-size:13px;line-height:22px}
.post-foot{display:flex;align-items:center;margin:8px 0 4px;height:30px}
.social{display:flex;gap:3px}
.social i{width:22px;height:22px;border-radius:3px}
.social .feed{background:var(--social-orange)}
.social .friends{background:var(--social-blue)}
.social .updates{background:var(--social-sky)}
.btn-more{margin-left:auto;width:110px;height:28px;line-height:28px;font-size:13px}
</style>
</head>
<body>
<div class="top-strip"></div>
<div class="header-band" role="img" aria-label="Dark stone texture with scattered footprint decorations"></div>
<div class="brand"><span class="brand-mark"></span><span class="brand-name">Pathwell</span></div>
<div class="tagline">Getting back on track</div>
<div class="footer-band" role="img" aria-label="Dark stone texture"></div>

<div class="site-frame">
  <nav class="main-nav">
    <a class="current" href="#">Home</a>
    <a href="#">About Us</a>
    <a href="#">Contact Us</a>
    <div class="search"><span>Search</span><i>
      <svg width="16" height="16" viewBox="0 0 16 16"><circle cx="6.5" cy="6.5" r="4.5" fill="none" stroke="#fff" stroke-width="2"/><line x1="10" y1="10" x2="14.5" y2="14.5" stroke="#fff" stroke-width="2.4"/></svg>
    </i></div>
  </nav>

  <aside class="column col-left">
    <section class="card">
      <div class="card-head">eBook</div>
      <div class="card-body ebook-body">"THE CLEAR MORNING PROMISE - The Gentle Path to finding calm and keeping it for good!"
        <span class="ebook-cover" role="img" aria-label="eBook cover"></span>
        <a class="btn btn-download" href="#">Download now</a>
      </div>
    </section>
    <div class="gap"></div>
    <section class="card">
      <div class="card-head">Ads</div>
      <div class="link-list ads-body"><h4>Ads by Adnetic</h4>
        <a href="#">luctus elementum.</a><a href="#">Vivamus eu</a><a href="#">purus a magna ad</a><a href="#">ipiscing gravida.</a><a href="#">Cras orci nulla,</a></div>
    </section>
    <div class="gap"></div>
    <section class="card">
      <div class="card-head">Links</div>
      <div class="link-list links-body"><h4>Other Blogs</h4>
        <a href="#">luctus elementum.</a><a href="#">Vivamus eu</a><a href="#">purus a magna ad</a><a href="#">ipiscing gravida.</a><a href="#">Cras orci nulla,</a></div>
    </section>
  </aside>

  <main class="column col-center">
    <section class="card">
      <div class="card-head">Welcome</div>
      <div class="welcome-body">Lorem ipsum dolor sit amet, consectetur adipiscing elit. Phasellus ornare venenatis rhoncus. Nullam ac massa ipsum. Ut vel nisl nisl. Nam et tellus justo. Pellentesque ut mollis est. Sed porta diam nec risus egestas mollis. Duis vestibulum felis at dui eleifend id posuere risus vulputate. Nulla mi elit, tempus sed iaculis a, fermentum at orci.</div>
    </section>
    <div class="gap" style="height:14px"></div>
    <section class="card">
      <div class="card-head">Blog</div>
      <div class="blog-body">
        <article>
          <h2 class="post-title">September 27th - October</h2>
          <p class="post-meta">Posted by <a href="#">admin</a> on Sep27 2010 | <a href="#">1 comment</a></p>
          <div class="post-row">
            <div class="post-photo" role="img" aria-label="Photo of a smiling couple"></div>
            <p class="post-text">luctus elementum. Vivamus eu purus a magna adipiscing gravida. Cras orci nulla, rhoncus ac viverra sed, volutpat nec massa. Curabitur dapibus, tellus ut molestie ornare,</p>
          </div>
          <div class="post-foot">
            <div class="social"><i class="feed"></i><i class="friends"></i><i class="updates"></i></div>
            <a class="btn btn-more" href="#">Read more</a>
          </div>
        </article>
        <article>
          <h2 class="post-title">September 23th - October</h2>
          <p class="post-meta" style="margin-bottom:6px">Posted by <a href="#">admin</a> on Sep23 2010 | <a href="#">1 comment</a></p>
          <p class="post-text">luctus elementum. Vivamus eu purus a magna adipiscing gravida. Cras orci nulla, rhoncus ac viverra sed, volutpat nec massa. Curabitur dapibus, tellus ut molestie ornare, diam sem sagittis sapien, facilisis dictum ligula velit ut neque. Donec in magna sit amet leo mollis sagittis id sed odio.</p>
          <div class="post-foot">
            <div class="social"><i class="feed"></i><i class="friends"></i><i class="updates"></i></div>
            <a class="btn btn-more" href="#">Read more</a>
          </div>
        </article>
      </div>
    </section>
  </main>

  <aside class="column col-right">
    <section class="card">
      <div class="card-head">eBook</div>
      <div class="card-body ebook-body">"THE CLEAR MORNING PROMISE - The Gentle Path to finding calm and keeping it for good!"
        <span class="ebook-cover" role="img" aria-label="eBook cover"></span>
        <a class="btn btn-download" href="#">Download now</a>
      </div>
    </section>
    <div class="gap"></div>
    <section class="card">
      <div class="card-head">Ads</div>
      <div class="link-list ads-body"><h4>Ads by Adnetic</h4>
        <a href="#">luctus elementum.</a><a href="#">Vivamus eu</a><a href="#">purus a magna ad</a><a href="#">ipiscing gravida.</a><a href="#">Cras orci nulla,</a></div>
    </section>
    <div class="gap" style="height:14px"></div>
    <section class="card">
      <div class="card-head">Links</div>
      <div class="link-list links-body"><h4>Other Blogs</h4>
        <a href="#">luctus elementum.</a><a href="#">Vivamus eu</a><a href="#">purus a magna ad</a><a href="#">ipiscing gravida.</a><a href="#">Cras orci nulla,</a></div>
    </section>
  </aside>
</div>
</body>
</html>
```